Educational Construction Organization needs Flyer for Upcoming Forum

We need a SAVE THE DATE Flyer for our 2020 Ravteq Forum. We work with Architects, Engineers, Contractors and Owners in the design and construction industry. Our mission is to evolve the capital projects industry through sharing of knowledge for optimized leadership, delivery and performance. The final design should communicate the connection between these industry professionals, our mission, and the Forum theme and byline.
Updates

Need extra days to review

Target Market(s)

Design and construction industry.

Industry/Entity Type

Construction

Font styles to use
Sans Serif

Colors

Designer to choose colors to be used in the design.

Requirements
Must have
• Title, By-line, 3 key topics, Date and location. Design that implements the theme with graphic(s) (not just text).
• NEW TITLE: FUTURE PROOFING: Connecting the dots to make sense of the "SMART" City
• 3 Key Topics: Smart Cities, Smart Institutions, Smart Connections
• Date: April 1-3, 2020
• Location: San Antonio, TX
Nice to have
• Please review attached problem statement for a better understanding of what this Forum will focus on when designing your graphic for the flyer.

```html
<!DOCTYPE html>
<html lang="en">
<head>
<meta charset="utf-8">
<title>Save the Date – 2020 Ravteq Forum</title>
<link rel="stylesheet" href="https://fonts.googleapis.com/css2?family=Roboto:wght@500;700;900&display=swap">
<style>
  :root {
    --stage: #3b3b3b;
    --navy-deep: #0a2640;
    --navy: #123a5c;
    --navy-light: #1f5f8a;
    --band: #1a6a96;
    --band-edge: #2b86b5;
    --sky-blue: #1a7fb8;
    --accent-blue: #2c8fd8;
    --soft-grey: #c9cdd2;
    --white: #ffffff;
    --icon-navy: #1d4766;
    --grass: #8cb43c;
    --brand-blue: #3b4ea0;
  }
  * { margin: 0; padding: 0; box-sizing: border-box; }
  html, body { width: 1200px; height: 1000px; overflow: hidden; }
  body {
    background: var(--stage);
    font-family: "Roboto", Arial, sans-serif;
    position: relative;
  }
  .flyer {
    position: absolute;
    left: 348px; top: 72px;
    width: 620px; height: 871px;
    overflow: hidden;
    background: radial-gradient(ellipse 70% 45% at 50% 38%, var(--navy-light) 0%, var(--navy) 55%, var(--navy-deep) 100%);
    color: var(--white);
  }
  .abs { position: absolute; }
  .circuit-art {
    left: 150px; top: 20px; width: 470px; height: 240px;
    background: radial-gradient(ellipse at 40% 40%, rgba(60,130,180,.35), rgba(20,60,95,0) 70%);
  }
  .topics-row { top: 28px; left: 18px; right: 20px; display: flex; justify-content: space-between;
    font-size: 16px; font-weight: 700; color: var(--sky-blue); letter-spacing: .2px; }
  .side-brand { left: 12px; top: 80px; width: 44px; height: 170px; }
  .side-brand .mark { position: absolute; left: 7px; top: 6px; width: 30px; height: 30px; border-radius: 50%; background: var(--white); }
  .side-brand .name { position: absolute; left: 22px; top: 48px; transform-origin: left top; transform: rotate(90deg) translateY(-50%);
    font-size: 26px; font-weight: 700; white-space: nowrap; }
  .headline { left: 310px; top: 64px; font-weight: 700; line-height: .88; }
  .headline .word { display: block; font-size: 90px; letter-spacing: -2px; }
  .headline .the { position: absolute; left: 222px; top: 10px; font-size: 22px; transform-origin: left top;
    transform: rotate(90deg) translateY(-100%); letter-spacing: 1px; }
  .event-date { left: 310px; top: 238px; font-size: 30px; font-weight: 700; }
  .event-place { left: 310px; top: 274px; font-size: 26px; font-weight: 500; }
  .forum-kicker { top: 320px; left: 0; width: 100%; text-align: center; font-size: 17px; font-weight: 700;
    letter-spacing: 3px; color: var(--accent-blue); }
  .forum-title { top: 342px; left: 0; width: 100%; text-align: center; font-size: 26px; font-weight: 700; color: var(--soft-grey); }
  .forum-title .smart { font-size: 34px; color: var(--accent-blue); }
  .byline { top: 392px; left: 0; width: 100%; text-align: center; font-size: 14px; font-weight: 500; color: var(--soft-grey); }
  .byline .lead { font-size: 17px; color: var(--accent-blue); font-weight: 700; }
  .explore { top: 442px; left: 0; width: 100%; text-align: center; font-size: 12.5px; font-weight: 500; color: var(--soft-grey); line-height: 1.35; letter-spacing: .3px; }
  .skyline-art { left: 0; top: 560px; width: 620px; height: 290px;
    background: linear-gradient(180deg, rgba(30,90,130,0) 0%, rgba(35,105,150,.6) 45%, #2a7aa8 100%); }
  .ground { left: 0; bottom: 0; width: 620px; height: 26px; background: var(--grass); }
  .graphics { left: 0; top: 0; width: 620px; height: 871px; }
  .topic-label { position: absolute; text-align: center; font-weight: 700; color: var(--icon-navy); line-height: 1.25; }
  .topic-cities { left: 49px; top: 516px; width: 140px; font-size: 19px; }
  .topic-connections { left: 185px; top: 614px; width: 150px; font-size: 17px; }
  .topic-institutions { left: 405px; top: 510px; width: 190px; font-size: 22px; }
  .city-icon { left: 68px; top: 572px; width: 103px; height: 85px; background: linear-gradient(180deg, #2d5878, var(--icon-navy)); }
  .closing-line { left: 28px; top: 738px; font-size: 21px; font-weight: 700; color: var(--soft-grey); white-space: nowrap; }
  .closing-line .smart { font-size: 25px; color: var(--accent-blue); }
  .corner-brand { right: 0; bottom: 0; width: 172px; height: 88px; background: var(--white);
    border-top-left-radius: 110px 88px; display: flex; align-items: center; justify-content: center; gap: 8px; padding-left: 14px; }
  .corner-brand .mark { width: 26px; height: 26px; border-radius: 50%; background: var(--brand-blue); }
  .corner-brand .name { font-size: 24px; font-weight: 700; color: var(--brand-blue); }
</style>
</head>
<body>
  <main class="flyer">
    <div class="abs circuit-art" role="img" aria-label="Network of connected technology icons and circuit lines"></div>
    <div class="abs skyline-art" role="img" aria-label="City skyline silhouette with connected digital icons"></div>
    <div class="abs ground"></div>

    <svg class="abs graphics" viewBox="0 0 620 871" aria-hidden="true">
      <polygon points="0,420 620,420 620,483 310,505 0,483" fill="var(--band)" opacity=".75"/>
      <polyline points="0,483 310,505 620,483" fill="none" stroke="var(--band-edge)" stroke-width="4"/>
      <polyline points="0,430 310,452 620,430" fill="none" stroke="var(--band-edge)" stroke-width="2" opacity=".4"/>
      <polyline points="499,669 499,692 320,692" fill="none" stroke="var(--white)" stroke-width="2.5"/>
      <circle cx="119" cy="591" r="92" fill="var(--white)" stroke="var(--navy)" stroke-width="3"/>
      <circle cx="499" cy="575" r="94" fill="var(--white)" stroke="var(--navy)" stroke-width="3"/>
      <circle cx="260" cy="635" r="73" fill="var(--white)" stroke="var(--navy)" stroke-width="3"/>
      <g class="wifi-icon" fill="none" stroke="var(--white)" stroke-width="3.5" stroke-linecap="round">
        <path d="M316 578 A8 8 0 0 1 324 586"/>
        <path d="M316 570 A16 16 0 0 1 332 586"/>
        <path d="M316 562 A24 24 0 0 1 340 586"/>
      </g>
      <circle cx="316" cy="586" r="2.8" fill="var(--white)"/>
      <g fill="var(--icon-navy)">
        <polygon points="499,580 529,594 469,594"/>
        <rect x="471" y="596" width="56" height="4"/>
        <rect x="476" y="602" width="8" height="22"/>
        <rect x="490" y="602" width="8" height="22"/>
        <rect x="502" y="602" width="8" height="22"/>
        <rect x="515" y="602" width="8" height="22"/>
        <rect x="469" y="626" width="60" height="5"/>
      </g>
    </svg>

    <div class="abs city-icon" role="img" aria-label="Cluster of city tower buildings"></div>

    <div class="abs topics-row">
      <span>SMART CITIES</span><span>SMART CONNECTIONS</span><span>SMART INSTITUTIONS</span>
    </div>

    <div class="abs side-brand"><span class="mark"></span><span class="name">Ravteq</span></div>

    <h1 class="abs headline">
      <span class="word">SAVE</span>
      <span class="the">THE</span>
      <span class="word">DATE</span>
    </h1>
    <p class="abs event-date">APRIL 1-3, 2020</p>
    <p class="abs event-place">San Antonio, TX</p>

    <p class="abs forum-kicker">FUTURE PROOFING:</p>
    <h2 class="abs forum-title">MAKING SENSE OF THE <span class="smart">SMART</span> CITY</h2>
    <p class="abs byline"><span class="lead">CONNECTING THE DOTS</span> FOR DYNAMIC PLANNING, DESIGN AND DELIVERY</p>
    <p class="abs explore">EXPLORE HOW THE BUILT ENVIRONMENT<br>CONNECTS THE DOTS TO ACHIEVE THESE GOALS</p>

    <div class="topic-label topic-cities">SMART<br>CITIES</div>
    <div class="topic-label topic-connections">SMART<br>CONNECTIONS</div>
    <div class="topic-label topic-institutions">SMART<br>INSTITUTIONS</div>

    <p class="abs closing-line"><span class="smart">SMART</span> CITY - WITH AN EYE ON CULTURAL AND ASPECTS</p>

    <div class="abs corner-brand"><span class="mark"></span><span class="name">Ravteq</span></div>
  </main>
</body>
</html>
```